Design a Dynamic and User-Friendly Website for qGuestly: Revolutionize Visitor Management

Description of qGuestly:

qGuestly is an innovative online visitor management system designed to streamline the process of managing visitors in various organizational settings. Our system automates the check-in process, enhances security by keeping accurate visitor logs, and ensures compliance with local regulations through customizable features. With functionalities such as contactless sign-in, real-time notifications, visitor badge printing, and comprehensive reporting, qGuestly provides a modern solution to traditional visitor management challenges.

Target Audience:

Our primary target audience includes businesses and institutions across Africa, starting with Nigeria. This includes corporate offices, educational institutions, healthcare facilities, and government buildings that are looking for efficient, secure, and scalable visitor management solutions. Our system is particularly tailored to meet the needs of facility managers, security personnel, and front desk staff who prioritize ease of use, data security, and operational efficiency. Additionally, qGuestly aims to cater to IT managers looking for robust systems that can seamlessly integrate with existing organizational infrastructure.

Color Scheme:

While specific colors are not mandated, the chosen palette should convey trust and stability, growth and efficiency, and maintain a professional and clean appearance. The colors selected should harmonize to create a welcoming, secure, and efficient atmosphere.
Typography:

Use modern, sans-serif fonts for readability and a contemporary look. Primary text should be clear with high contrast against the background, and headings can be bold to create a hierarchical structure that is easy to navigate.
Imagery:

Photography: High-quality images that feature African professionals and contexts, illustrating diverse, professional scenarios relevant to our target industries (such as corporate offices, educational institutions, healthcare facilities). Photos should authentically represent the African demographic, showing interactions between people and technology, emphasizing the ease and security of the visitor management process.
Illustrations: Custom illustrations that should culturally resonate with African settings and characters, vividly depicting functionalities of qGuestly such as scanning a QR code, receiving a visitor badge, or receiving alerts on a smartphone or desktop. These illustrations should adopt a style that complements the overall design aesthetic of the site.
Layout and Design Elements:

A clean, minimalistic layout that focuses on usability with easy navigation paths for all user types.
Use cards or tiles for different sections such as features, testimonials, or case studies, which can help organize information cleanly and attractively.
Consider interactive elements like hover effects, animated transitions for loading elements, and subtle animations in illustrations to make the user experience dynamic and engaging.
Overall Theme:

The theme should be professional and welcoming, reflecting a high-tech solution that is approachable for users with varying levels of tech expertise. The design should instill confidence in the security and efficiency of the system, while also being culturally appropriate and user-friendly to encourage interaction and exploration of the site’s content.
This style and theme guide emphasizes flexibility in color usage while maintaining clear directives on the emotional and functional responses the design should invoke, ensuring it aligns with the values and needs of qGuestly's target audience.

What websites can designers draw inspiration from?
List websites you like and describe what you like about them.

https://entrypadhub.example/en-usremove
same industry so you can see their approaches to marketing to similar customers - granted their target is not specific to african market Very clean design and straight to the point. Their feature set is closest to our feature set.
http://www.gatelumo.exampleremove
clean design and straight to the point
http://lobbirant.exampleremove

Home Page
-------------------
Main Goal: Encourage visitors to start their 15-day free trial, effectively converting them into leads or potential customers.

Content Layout:
Hero Section: Engaging hero image or video that shows the qGuestly system in action, with clear, prominent call-to-action (CTA) buttons for "Start your 15 day free trial" and secondary CTA for "Buy now"

Product Overview: Quick introduction to what qGuestly is and its key benefits, such as enhanced security, easy integration, and improved operational efficiency.

Features Highlight: Brief visuals or icons depicting major features like contactless sign-in, real-time alerts, and comprehensive reporting.

How It Works: A concise step-by-step guide or graphic explaining how to get started with qGuestly.

CTA Section: A more detailed call to action for starting the free trial,
if they want a more hands on guide allow them to schedule a demo and if they are ready click purchase to buy now.
Footer: Navigation links to other site sections, social media links, and legal information.

-------------------
Pricing Page
-------------------
Main Goal: Clearly convey the pricing structure in a way that users can easily understand and compare options based on their location and specific needs.

Content Layout:

Pricing Introduction: Explain the subscription model, highlighting the flexibility and scalability of the service (i.e., per location and additional tablets).

Country-Specific Pricing Tabs: Tabs or a dropdown menu allowing users to choose their country (Nigeria, Ghana, South Africa, Kenya) to view localized pricing in the respective currencies (NGN, GHS, ZAR, KES).
Subscription Per Location: Detailed pricing for managing a single location, with benefits listed beside the price

Tablets and Data Plans: A clear breakdown of the cost per tablet and the associated wireless data plans, including bulk discount options if applicable.
Interactive Pricing Calculator: A tool that allows users to calculate their monthly cost based on the number of locations and tablets they plan to use.

Add ons - for hardware, etc

FAQs: A section dedicated to frequently asked questions specifically about pricing, billing cycles, and cancellation policies.

CTA: Strong call to action for starting a free trial, with an emphasis on the ease of signing up and the no-commitment nature of the trial.

Footer: Standard navigational links, contact information, and social media buttons.

-------------------
Feature Page Template
-------------------
Main Goal: To detail individual features of qGuestly, demonstrating the functionality and benefits to help prospective clients understand the value provided.

Content Layout:
Feature Introduction: Large title with a succinct description of the feature.

In-depth Details: Bullet points or short paragraphs explaining the feature, supported by relevant images or icons.

Use Case Scenario: Real-world application or a mini-case study showing the feature in action.

Benefit Summary: A list or graphic illustrating the benefits of the feature.

CTA: Prompt to try this feature via signup or schedule a demo speak with a sales representative.

Footer: Standard links and social media connections.

-------------------
Blog Page
-------------------
Main Goal: To engage current and prospective clients with useful content, position qGuestly as a thought leader in the visitor management space, and improve SEO rankings.

Content Layout:
Featured Article: Highlight a recent or popular post prominently at the top.

Article List: Thumbnails and summaries of additional articles with clear categorization (e.g., Tips, Case Studies, Industry News).

Search and Filter Tools: Allow users to filter blog posts by topic, date, etc.

Newsletter Signup: Encourage visitors to subscribe to updates.
Social Share Buttons: Enable easy sharing of articles.
Footer: Include a comprehensive footer with navigational links and contact info.

Generic Content Page (e.g., Contact Us, About Us)
------------------------------
Main Goal: To provide essential information about the qGuestly company or to facilitate contact with the company.

Content Layout:
Page Title and Introduction: Clear heading with a brief paragraph summarizing the page’s purpose.

Main Content Area: Detailed content appropriate to the page (e.g., company history, team bios for About Us; contact form, map, and helpline numbers for Contact Us).

Sidebar/Additional Elements: For Contact Us, include operational hours or a quick FAQ. For About Us, list awards or recognitions.

CTA: Depending on the page, direct users to other parts of the site (e.g., careers page link on About Us, newsletter sign-up on Contact Us).
Footer: Standard footer with expanded company details if on the Contact Us page.

Coding

```html
<!DOCTYPE html>
<html lang="en">
<head>
<meta charset="utf-8">
<title>qGuestly — Visitor management</title>
<link href="https://fonts.googleapis.com/css2?family=Lexend:wght@400;500;600;700&family=DM+Sans:wght@400;500;700&display=swap" rel="stylesheet">
<style>
:root{
  --indigo:#2c10ad;
  --indigo-deep:#22108f;
  --ink:#1a1545;
  --muted:#8b89a6;
  --cyan:#22b8ec;
  --navy:#0e0b4b;
  --band:#f4f5f8;
  --wave:#d9dde4;
  --line:#e6e7ef;
  --white:#ffffff;
}
*{box-sizing:border-box;margin:0;padding:0}
html,body{width:1200px;height:3778px;overflow:hidden}
body{background:var(--white);font-family:"DM Sans",sans-serif;color:var(--ink);position:relative}
.abs{position:absolute}
.head{font-family:"Lexend",sans-serif}
.accent{color:var(--indigo)}

/* header */
.site-header{left:0;top:0;width:1200px;height:64px;background:var(--white);box-shadow:0 4px 16px rgba(40,30,120,.06);z-index:2}
.brand{display:flex;align-items:center;gap:10px;font-family:"Lexend",sans-serif;font-weight:700;font-size:30px;color:var(--indigo);letter-spacing:-.5px}
.brand-dot{width:18px;height:18px;border-radius:50%;background:var(--cyan)}
.site-header .brand{left:94px;top:12px}
.nav{left:489px;top:22px;display:flex;gap:30px;font-size:11.5px;color:var(--ink)}
.nav a{color:inherit;text-decoration:none}
.nav a.current{color:var(--indigo);border-bottom:2px solid var(--cyan);padding-bottom:3px}

/* buttons */
.btn{display:inline-flex;align-items:center;justify-content:center;height:37px;font-size:11.5px;font-weight:700;border-radius:3px;text-decoration:none}
.btn-primary{background:var(--indigo);color:var(--white);width:203px;box-shadow:3px 3px 0 rgba(44,16,173,.25)}
.btn-cyan{background:var(--cyan);color:var(--white);width:203px;box-shadow:3px 3px 0 rgba(34,184,236,.3)}
.btn-outline{border:1.5px solid var(--indigo);color:var(--indigo);width:115px;background:var(--white);box-shadow:3px 3px 0 rgba(44,16,173,.12)}
.btn-pair{display:flex;gap:13px}
.header-cta{left:906px;top:12px;width:203px;height:39px}

/* hero */
.hero-glow{left:0;top:64px;width:1200px;height:700px;background:
  radial-gradient(ellipse 360px 200px at 0 160px,rgba(200,190,255,.22),transparent 70%),
  radial-gradient(ellipse 380px 220px at 1200px 280px,rgba(190,225,230,.25),transparent 70%)}
.hero-title{left:0;top:133px;width:1200px;text-align:center;font-size:38px;font-weight:600;line-height:46px;color:var(--ink)}
.hero-actions{left:434px;top:253px}
.hero-media{left:199px;top:343px;width:801px;height:377px;border:2px solid #b9aef0;border-radius:10px;overflow:hidden;
  background:linear-gradient(100deg,#e9eaec 0%,#d3d4d6 35%,#9ea39a 62%,#cfd2cc 100%);box-shadow:0 24px 50px rgba(60,40,160,.12)}
.play{left:369px;top:160px;width:56px;height:56px}

/* section heads */
.sec-title{left:0;width:1200px;text-align:center;font-size:28px;font-weight:500}
.sec-lead{left:300px;width:600px;text-align:center;font-size:11.5px;line-height:20px;color:var(--muted)}

/* overview */
.benefit{width:300px}
.benefit .art{width:207px;height:160px;border-radius:8px;background:linear-gradient(135deg,#eef0ff,#d9dcfb 60%,#c5e9f7)}
.benefit h3{font-family:"Lexend",sans-serif;font-size:17.5px;font-weight:400;margin-top:27px;color:var(--ink)}
.benefit p{font-size:10.5px;line-height:20px;color:var(--muted);margin-top:10px;width:280px}

/* features band */
.band{left:0;top:1340px;width:1200px;height:680px}
.feature-card{top:1568px;width:248px;height:238px;background:var(--white);border-radius:4px;box-shadow:0 6px 24px rgba(30,30,80,.07);text-align:center}
.feature-card .ic{margin:32px auto 0;width:64px;height:64px;border-radius:50%;background:radial-gradient(circle at 50% 40%,#eceaff,rgba(236,234,255,0) 70%);display:flex;align-items:center;justify-content:center}
.feature-card h3{font-size:14px;font-weight:700;margin-top:20px}
.feature-card p{font-size:10.5px;line-height:19px;color:var(--muted);margin:12px 24px 0}

/* steps */
.step-art{width:170px;height:170px;border-radius:10px}
.step-art.rose{background:linear-gradient(135deg,#fde9e6,#e9e8f6)}
.step-art.sky{background:linear-gradient(135deg,#e8f1f8,#e9e8f6)}
.step-art.mint{background:linear-gradient(135deg,#e4f6ee,#e9e8f6)}
.step-art.sand{background:linear-gradient(135deg,#fdf0e4,#e9e8f6)}
.step-text h3{font-family:"Lexend",sans-serif;font-size:21px;font-weight:400;color:var(--indigo)}
.step-text p{font-size:11.5px;line-height:19.5px;color:var(--ink);margin-top:10px;width:330px}

/* banner */
.footer-bg{left:0;top:3300px;width:1200px;height:478px;background:var(--band)}
.trial-banner{left:92px;top:3190px;width:1015px;height:228px;background:var(--navy);border-radius:70px 0 70px 0;text-align:center}
.trial-banner h2{font-family:"Lexend",sans-serif;font-weight:700;font-size:38px;margin-top:50px;color:var(--cyan)}
.trial-banner h2 span{color:#3a23c4}
.trial-banner p{font-size:20px;color:#d6d5ee;margin-top:8px}
.trial-banner .btn{margin-top:16px;height:35px}

/* footer */
.site-footer .brand{left:94px;top:3504px;font-size:38px}
.socials{left:186px;top:3584px;display:flex;gap:8px}
.socials span{width:32px;height:32px;border-radius:50%;border:1.5px solid var(--indigo);background:var(--white)}
.socials span.on{background:var(--cyan);border-color:var(--cyan)}
.foot-col h4{font-size:13px;font-weight:700;color:var(--ink)}
.foot-col ul{list-style:none;margin-top:20px}
.foot-col li{font-size:10px;color:var(--muted);line-height:20px}
.contact-row{display:flex;gap:10px;font-size:12px;color:var(--muted);margin-top:18px}
.contact-row.small{font-size:10px;line-height:16px}
.contact-row b{color:var(--indigo);font-weight:500}
.sub-input{width:332px;height:30px;border:1px solid #cfd0de;border-radius:3px;background:var(--white);font-size:9.5px;color:var(--muted);padding:0 10px;display:flex;align-items:center;margin-top:12px}
.sub-send{width:88px;height:31px;border:1.5px solid var(--indigo);border-radius:3px;color:var(--indigo);font-size:11.5px;font-weight:700;display:flex;align-items:center;justify-content:center;margin-top:14px;background:var(--white)}
.legal{top:3738px;font-size:10px;color:var(--muted)}
.legal b{color:var(--indigo)}
</style>
</head>
<body>

<!-- header -->
<header class="abs site-header">
  <div class="abs brand"><span class="brand-dot"></span>qGuestly</div>
  <nav class="abs nav">
    <a class="current" href="#">Home</a><a href="#">Feature</a><a href="#">Pricing</a><a href="#">About us</a><a href="#">Blog</a><a href="#">Contact us</a>
  </nav>
  <a class="abs btn btn-primary header-cta" href="#">Start your 15 day free trial</a>
</header>

<!-- hero -->
<div class="abs hero-glow"></div>
<h1 class="abs head hero-title"><span class="accent">Customizable sign in software</span> for<br>your workplace</h1>
<div class="abs btn-pair hero-actions">
  <a class="btn btn-cyan" href="#">Start your 15 day free trial</a>
  <a class="btn btn-outline" href="#">Buy now!</a>
</div>
<div class="abs hero-media" role="img" aria-label="Product video still: a smiling professional checking in on a smartphone in a bright office">
  <svg class="abs play" viewBox="0 0 56 56"><circle cx="28" cy="28" r="27" fill="rgba(120,120,220,.35)"/><circle cx="28" cy="28" r="17" fill="rgba(44,16,173,.75)"/><path d="M24 20l10 8-10 8z" fill="#22b8ec"/></svg>
</div>

<!-- product overview -->
<h2 class="abs head sec-title accent" style="top:790px">Product overview</h2>
<p class="abs sec-lead" style="top:846px">Lorem Ipsum has been the industry's standard dummy text ever since the 1500s, when an unknown printer took a galley of type and scrambled it to make a type specimen book.</p>

<div class="abs benefit" style="left:92px;top:921px">
  <div class="art" role="img" aria-label="Illustration of a person beside a phone with a security shield"></div>
  <h3>Enhanced security</h3>
  <p>Lorem ipsum dolor sit amet, consectetur adipis elit, sed do eiusmod tempor incididunt ut labore et dolore magna aliqua. Quis ipsum...</p>
</div>
<div class="abs benefit" style="left:442px;top:921px">
  <div class="art" role="img" aria-label="Illustration of people working with connected dashboards"></div>
  <h3>Easy integration</h3>
  <p>Lorem ipsum dolor sit amet, consectetur adipis elit, sed do eiusmod tempor incididunt ut labore et dolore magna aliqua. Quis ipsum...</p>
</div>
<div class="abs benefit" style="left:793px;top:921px">
  <div class="art" role="img" aria-label="Isometric illustration of a team running efficient workflows"></div>
  <h3>Improved operational efficiency</h3>
  <p>Lorem ipsum dolor sit amet, consectetur adipis elit, sed do eiusmod tempor incididunt ut labore et dolore magna aliqua. Quis ipsum...</p>
</div>
<div class="abs btn-pair" style="left:434px;top:1227px">
  <a class="btn btn-primary" href="#">Start your 15 day free trial</a>
  <a class="btn btn-outline" href="#">Buy now!</a>
</div>

<!-- features band -->
<svg class="abs band" viewBox="0 0 1200 680" preserveAspectRatio="none">
  <path d="M0 86 C250 70 420 10 620 8 C820 6 930 50 1200 40 L1200 56 C930 66 820 22 620 24 C420 26 250 86 0 100Z" fill="var(--wave)"/>
  <path d="M0 100 C250 86 420 26 620 24 C820 22 930 66 1200 56 L1200 560 C1000 600 850 640 620 648 C400 656 250 600 0 585Z" fill="var(--band)"/>
  <path d="M0 585 C250 600 400 656 620 648 C850 640 1000 600 1200 560 L1200 576 C1000 616 850 660 620 666 C400 672 250 620 0 600Z" fill="var(--wave)"/>
</svg>

<h2 class="abs head sec-title" style="top:1452px">qGuestly <span class="accent">features</span></h2>
<p class="abs sec-lead" style="top:1507px">Lorem Ipsum has been the industry's standard dummy text ever since the 1500s, when an unknown printer took a galley of type and scrambled it to make a type specimen book.</p>

<div class="abs feature-card" style="left:201px">
  <div class="ic"><svg width="30" height="40" viewBox="0 0 30 40" fill="none" stroke="var(--ink)" stroke-width="2"><rect x="4" y="2" width="22" height="36" rx="3"/><circle cx="15" cy="16" r="5"/><path d="M9 27h12M12 33h6"/></svg></div>
  <h3>Contactless Sign-in</h3>
  <p>Lorem ipsum dolor sit amet, consectetur adipiscing elit, Nulla tincidunt, eiusmod tempor.</p>
</div>
<div class="abs feature-card" style="left:476px">
  <div class="ic"><svg width="40" height="40" viewBox="0 0 40 40" fill="none" stroke="var(--ink)" stroke-width="2"><path d="M10 30V18a10 10 0 0 1 20 0v12M6 30h28M16 34a4 4 0 0 0 8 0M20 4v4"/><circle cx="31" cy="10" r="5" fill="var(--indigo)" stroke="none"/></svg></div>
  <h3>Real-Time Alerts</h3>
  <p>Lorem ipsum dolor sit amet, consectetur adipiscing elit, Nulla tincidunt, eiusmod tempor.</p>
</div>
<div class="abs feature-card" style="left:750px">
  <div class="ic"><svg width="38" height="40" viewBox="0 0 38 40" fill="none" stroke="var(--ink)" stroke-width="2"><rect x="4" y="2" width="26" height="34" rx="2"/><path d="M9 9h16M9 14h10"/><path d="M12 32v-6M18 32v-10M24 32v-8" stroke="var(--indigo)" stroke-width="3"/></svg></div>
  <h3>Comprehensive Reporting</h3>
  <p>Lorem ipsum dolor sit amet, consectetur adipiscing elit, Nulla tincidunt, eiusmod tempor.</p>
</div>
<div class="abs btn-pair" style="left:434px;top:1841px">
  <a class="btn btn-primary" href="#">Start your 15 day free trial</a>
  <a class="btn btn-outline" href="#">Buy now!</a>
</div>

<!-- how it works -->
<h2 class="abs head sec-title" style="top:2080px">How it <span class="accent">works</span></h2>
<p class="abs sec-lead" style="top:2124px">Lorem Ipsum has been the industry's standard dummy text</p>

<div class="abs step-art rose" style="left:310px;top:2185px" role="img" aria-label="Line illustration of a browser window showing a visitor profile for contactless sign-in"></div>
<div class="abs step-text" style="left:517px;top:2228px">
  <h3>Contactless sign-in</h3>
  <p>There are many variations of passages of Lorem Ipsum available, but the majority have suffered alteration in som form, by injected randomised words which.</p>
</div>

<div class="abs step-text" style="left:331px;top:2436px">
  <h3>Real-time notifications</h3>
  <p>There are many variations of passages of Lorem Ipsum available, but the majority have suffered alteration in som form, by injected randomised words which.</p>
</div>
<div class="abs step-art sky" style="left:720px;top:2395px" role="img" aria-label="Line illustration of a notification bell with a message card"></div>

<div class="abs step-art mint" style="left:310px;top:2625px" role="img" aria-label="Line illustration of a printed visitor badge"></div>
<div class="abs step-text" style="left:517px;top:2660px">
  <h3>Visitor badge printing</h3>
  <p>There are many variations of passages of Lorem Ipsum available, but the majority have suffered alteration in som form, by injected randomised words which.</p>
</div>

<div class="abs step-text" style="left:331px;top:2878px">
  <h3>Comprehensive reporting</h3>
  <p>There are many variations of passages of Lorem Ipsum available, but the majority have suffered alteration in som form, by injected randomised words which.</p>
</div>
<div class="abs step-art sand" style="left:720px;top:2845px" role="img" aria-label="Line illustration of a report document"></div>

<div class="abs btn-pair" style="left:434px;top:3069px">
  <a class="btn btn-primary" href="#">Start your 15 day free trial</a>
  <a class="btn btn-outline" href="#">Buy now!</a>
</div>

<!-- trial banner and footer -->
<div class="abs footer-bg"></div>
<section class="abs trial-banner">
  <h2><span>Start your</span> 15 day free trial</h2>
  <p>Join over 8,000+ workplaces already working smarter with qGuestly</p>
  <a class="btn btn-cyan" href="#">Start your 15 day free trial</a>
</section>

<footer class="site-footer">
  <div class="abs brand"><span class="brand-dot"></span>qGuestly</div>
  <div class="abs socials" aria-label="Social media links"><span></span><span class="on"></span><span></span><span></span></div>

  <div class="abs foot-col" style="left:350px;top:3500px">
    <h4>Contact us</h4>
    <div class="contact-row">
      <svg width="12" height="12" viewBox="0 0 12 12"><path d="M2 1l2.5 0 1 3-1.5 1a6 6 0 0 0 3 3l1-1.5 3 1V10a1 1 0 0 1-1 1A9 9 0 0 1 1 2a1 1 0 0 1 1-1z" fill="var(--indigo)"/></svg>
      <span>+1 (555) 014-2290</span>
    </div>
    <div class="contact-row small">
      <svg width="12" height="12" viewBox="0 0 12 12"><rect x="1" y="2.5" width="10" height="7" fill="var(--indigo)"/><path d="M1 3l5 3.5L11 3" stroke="#fff" fill="none"/></svg>
      <span>hello@qguestly.example</span>
    </div>
    <div class="contact-row small">
      <svg width="12" height="14" viewBox="0 0 12 14"><path d="M6 13s-5-5-5-8a5 5 0 0 1 10 0c0 3-5 8-5 8z" fill="var(--indigo)"/><circle cx="6" cy="5" r="2" fill="#fff"/></svg>
      <span><b>qGuestly</b><br>418 Harlow Ave, Lakeview,<br>ST 20411, Westland</span>
    </div>
  </div>

  <div class="abs foot-col" style="left:592px;top:3500px">
    <h4>Quick Links</h4>
    <ul><li>Home</li><li>Feature</li><li>Pricing</li><li>About us</li><li>Blog</li><li>Contact us</li></ul>
  </div>

  <div class="abs foot-col" style="left:775px;top:3500px">
    <h4>Subscribe to Newsletter</h4>
    <p style="font-size:9.5px;line-height:17px;color:var(--muted);margin-top:14px;width:300px">Enter your email address to register to our newsletter subscription!</p>
    <div class="sub-input">Enter your email...</div>
    <div class="sub-send">Send</div>
  </div>

  <p class="abs legal" style="left:94px">© 2024 <b>qGuestly.</b> All right reserved</p>
  <p class="abs legal" style="left:592px">Terms and Conditions &nbsp;&nbsp;|&nbsp;&nbsp; Privacy Policy</p>
  <svg class="abs" style="left:1096px;top:3736px" width="14" height="14" viewBox="0 0 14 14" aria-label="Back to top"><path d="M7 1l6 12-6-3-6 3z" fill="var(--indigo)"/></svg>
</footer>

</body>
</html>
```